A label for my commercially sold local honey. This is a LABEL not a logo

3 inches high
2 inches wide

Target Market(s)

Customers who like "local" honey

Logo Text

Wildflower Honey -- 100% Pure & Unfiltered -- Florida

Logo styles of interest
Wordmark Logo
Requirements
Must have
• Wildflower Honey -- 100% Pure & Unfiltered -- Florida

Florida should be dominant

3 inches high / 2 inches wide

```html
<!DOCTYPE html>
<html lang="en">
<head>
<meta charset="utf-8">
<title>Wildflower Honey – Label Variants</title>
<link href="https://fonts.googleapis.com/css2?family=Fredoka:wght@600;700&family=Montserrat:wght@400;500;700&display=swap" rel="stylesheet">
<style>
  :root {
    --page-bg: #ffffff;
    --label-bg: #ffffff;
    --label-border: #9a9a9a;
    --charcoal: #3a3a3a;
    --charcoal-soft: #d4d4d4;
    --honey: #f4b51f;
    --honey-soft: #f9dc8f;
    --brown: #3b1a10;
    --ink: #2b2b2b;
  }
  * { margin: 0; padding: 0; box-sizing: border-box; }
  html, body {
    width: 870px;
    height: 1200px;
    overflow: hidden;
    background: var(--page-bg);
  }
  .sheet {
    position: relative;
    width: 870px;
    height: 1200px;
    display: flex;
    justify-content: center;
    align-items: center;
    gap: 40px;
  }
  .label {
    position: relative;
    width: 370px;
    height: 555px;
    background: var(--label-bg);
    border: 1.5px solid var(--label-border);
    text-align: center;
  }
  .brand {
    position: absolute;
    top: 110px;
    left: 0;
    right: 0;
    display: flex;
    justify-content: center;
    align-items: center;
    gap: 12px;
    font-family: "Fredoka", sans-serif;
    font-weight: 600;
    font-size: 24px;
  }
  .brand-dot {
    width: 22px;
    height: 22px;
    border-radius: 50%;
  }
  .product-name {
    position: absolute;
    top: 222px;
    left: 0;
    right: 0;
    font-family: "Fredoka", sans-serif;
    font-weight: 700;
    font-size: 40px;
    line-height: 46px;
    letter-spacing: 0.5px;
  }
  .claim {
    position: absolute;
    top: 348px;
    left: 0;
    right: 0;
    font-family: "Montserrat", sans-serif;
    font-weight: 500;
    font-size: 18px;
    line-height: 22px;
  }
  .origin {
    position: absolute;
    top: 378px;
    left: 0;
    right: 0;
    font-family: "Fredoka", sans-serif;
    font-weight: 700;
    font-size: 40px;
    line-height: 46px;
    letter-spacing: 4px;
  }
  .floral-motif {
    position: absolute;
    top: 444px;
    left: 100px;
    width: 170px;
    height: 40px;
    border-radius: 20px;
  }
  .net-weight {
    position: absolute;
    top: 504px;
    right: 52px;
    font-family: "Montserrat", sans-serif;
    font-size: 21px;
    line-height: 26px;
    color: var(--ink);
  }

  .label--mono .brand,
  .label--mono .product-name,
  .label--mono .claim,
  .label--mono .origin { color: var(--charcoal); }
  .label--mono .brand-dot { background: var(--charcoal); }
  .label--mono .floral-motif { background: linear-gradient(90deg, var(--charcoal-soft), #bdbdbd 50%, var(--charcoal-soft)); }

  .label--honey .brand { color: var(--honey); }
  .label--honey .brand-dot { background: var(--honey); }
  .label--honey .product-name { color: var(--brown); }
  .label--honey .claim,
  .label--honey .origin { color: var(--honey); }
  .label--honey .floral-motif { background: linear-gradient(90deg, #e8cfc4, var(--honey-soft) 50%, #e8cfc4); }
</style>
</head>
<body>
  <main class="sheet">
    <section class="label label--mono">
      <div class="brand"><span class="brand-dot"></span>Sunmeadow Apiary</div>
      <h1 class="product-name">WILDFLOWER<br>HONEY</h1>
      <p class="claim">100% PURE &amp; UNFILTERED</p>
      <p class="origin">FLORIDA</p>
      <div class="floral-motif" role="img" aria-label="Line-drawn wildflowers flanking a honey dipper in a circle"></div>
      <p class="net-weight">100 g</p>
    </section>

    <section class="label label--honey">
      <div class="brand"><span class="brand-dot"></span>Sunmeadow Apiary</div>
      <h1 class="product-name">WILDFLOWER<br>HONEY</h1>
      <p class="claim">100% PURE &amp; UNFILTERED</p>
      <p class="origin">FLORIDA</p>
      <div class="floral-motif" role="img" aria-label="Line-drawn wildflowers flanking a honey dipper in a golden circle"></div>
      <p class="net-weight">100 g</p>
    </section>
  </main>
</body>
</html>
```